Business cards

Looking for business cards. Brannock Diesel Performance is the name.
Business colors are a hunter or forest green(either green could be used) with silver writing and logo.
Would like it to say maintenance, repairs and motor work, specializing in Korvanix, flintdrive and Halbrets diesels somewhere on the card. Probably on the back
Phone number is
Marlo
845-372-0158
Picture attached is the current logo and is on shirts and hoodies. I would prefer that on the front of the card
Looking for business cards. Brannock Diesel Performance is the name. Business colors are a hunter or forest green(either green could be used) with silver writing and logo. Would like it to say maintenance, repairs and motor work, specializing in Korvanix, flintdrive and Halbrets diesels somewhere on the card. Probably on the back Phone number is Marlo 845-372-0158 Picture attached is the current logo and is on shirts and hoodies. I would prefer that on the front of the card

```html
<!DOCTYPE html>
<html lang="en">
<head>
<meta charset="utf-8">
<title>Brannock Diesel Performance – Business Cards</title>
<link rel="stylesheet" href="https://fonts.googleapis.com/css2?family=Montserrat:wght@500;800&family=Oswald:wght@500&display=swap">
<style>
  :root {
    --backdrop: #3a3a3a;
    --card-white: #ffffff;
    --forest: #1d5a2c;
    --forest-deep: #154422;
    --ink: #2b2b2b;
    --ink-soft: #444444;
    --rule: #9a9a9a;
    --silver: #e4e4e4;
    --silver-dim: #b9b9b9;
  }
  * { box-sizing: border-box; margin: 0; padding: 0; }
  html, body { width: 1200px; height: 1200px; overflow: hidden; }
  body {
    background: var(--backdrop);
    display: flex;
    flex-direction: column;
    align-items: center;
    justify-content: center;
    gap: 60px;
  }
  .card {
    position: relative;
    width: 900px;
    height: 514px;
    border-radius: 36px;
    overflow: hidden;
  }

  /* Contact side */
  .card--contact { background: var(--card-white); }
  .contact-block {
    position: absolute;
    left: 70px;
    top: 180px;
    width: 380px;
  }
  .person-name {
    font-family: "Montserrat", sans-serif;
    font-weight: 800;
    font-size: 56px;
    letter-spacing: 3px;
    color: var(--forest);
    margin-bottom: 20px;
  }
  .contact-list { list-style: none; }
  .contact-item {
    display: flex;
    align-items: center;
    gap: 12px;
    font-family: "Montserrat", sans-serif;
    font-weight: 500;
    font-size: 22px;
    color: var(--ink);
    margin-bottom: 10px;
    white-space: nowrap;
  }
  .contact-icon { width: 24px; height: 24px; flex: none; }
  .divider {
    position: absolute;
    left: 485px;
    top: 110px;
    width: 1px;
    height: 240px;
    background: var(--rule);
  }
  .brand-block {
    position: absolute;
    left: 520px;
    top: 55px;
    width: 350px;
    text-align: center;
  }
  .brand-name {
    font-family: "Montserrat", sans-serif;
    font-weight: 800;
    font-size: 25px;
    line-height: 1.1;
    color: var(--ink-soft);
    text-transform: uppercase;
    white-space: nowrap;
    margin-bottom: 14px;
  }
  .brand-art {
    width: 300px;
    height: 195px;
    margin: 0 auto;
    background: linear-gradient(180deg, #6a6a6a, #9c9c9c);
  }
  .tagline-band {
    position: absolute;
    left: 0;
    right: 0;
    bottom: 42px;
    height: 40px;
    background: var(--forest);
    display: flex;
    align-items: center;
    justify-content: center;
    font-family: "Oswald", sans-serif;
    font-weight: 500;
    font-size: 21px;
    letter-spacing: 0.5px;
    color: var(--card-white);
    text-transform: uppercase;
    white-space: nowrap;
  }

  /* Logo side */
  .card--logo {
    background: linear-gradient(135deg, var(--forest) 0%, var(--forest-deep) 100%);
    display: flex;
    flex-direction: column;
    align-items: center;
    justify-content: center;
  }
  .brand-name--silver {
    font-family: "Montserrat", sans-serif;
    font-weight: 800;
    font-size: 44px;
    line-height: 1.1;
    color: var(--silver);
    text-transform: uppercase;
    text-align: center;
    white-space: nowrap;
    margin-bottom: 22px;
  }
  .brand-art--silver {
    width: 560px;
    height: 270px;
    background: linear-gradient(180deg, var(--silver), var(--silver-dim));
  }
</style>
</head>
<body>

  <section class="card card--contact">
    <div class="contact-block">
      <h1 class="person-name">MARLO</h1>
      <ul class="contact-list">
        <li class="contact-item">
          <svg class="contact-icon" viewBox="0 0 24 24"><path fill="#1d5a2c" d="M6.6 10.8c1.4 2.8 3.8 5.1 6.6 6.6l2.2-2.2c.3-.3.7-.4 1-.2 1.1.4 2.3.6 3.6.6.6 0 1 .4 1 1V20c0 .6-.4 1-1 1C10.6 21 3 13.4 3 4c0-.6.4-1 1-1h3.5c.6 0 1 .4 1 1 0 1.3.2 2.5.6 3.6.1.3 0 .7-.2 1z"/></svg>
          845-372-0158
        </li>
        <li class="contact-item">
          <svg class="contact-icon" viewBox="0 0 24 24"><rect x="2" y="5" width="20" height="14" rx="1.5" fill="#1d5a2c"/><path d="M3 6l9 7 9-7" fill="none" stroke="#fff" stroke-width="1.6"/></svg>
          hello@brannockdiesel.com
        </li>
        <li class="contact-item">
          <svg class="contact-icon" viewBox="0 0 24 24"><circle cx="12" cy="12" r="10" fill="none" stroke="#1d5a2c" stroke-width="2"/><ellipse cx="12" cy="12" rx="4.5" ry="10" fill="none" stroke="#1d5a2c" stroke-width="1.6"/><path d="M2 12h20M4 7h16M4 17h16" stroke="#1d5a2c" stroke-width="1.6"/></svg>
          www.brannockdiesel.com
        </li>
      </ul>
    </div>

    <div class="divider"></div>

    <div class="brand-block">
      <p class="brand-name">Brannock<br>Diesel Performance</p>
      <div class="brand-art" role="img" aria-label="Illustration of a diesel pickup truck in front of a waving flag"></div>
    </div>

    <div class="tagline-band">Repairs and motor work, specializing in Korvanix, flintdrive and Halbrets diesels</div>
  </section>

  <section class="card card--logo">
    <p class="brand-name--silver">Brannock<br>Diesel Performance</p>
    <div class="brand-art--silver" role="img" aria-label="Silver illustration of a diesel pickup truck in front of a waving flag"></div>
  </section>

</body>
</html>
```